VFX Company Business Card Design Project

The Ember Vale is a decentralized Visual Effects Studio servicing the television and feature film industries.
Project Brief:
Take our logo that was previously designed on Pixel Harbor and make a double sided business card.
Requirements:
- Card MUST be double sided.
- Front of card MUST have the yellow part of our logo against the dark grey background.
- Back of card is completely up to the designer.
- Back of card must include the complete company logo.
Please follow these File Preparation guidelines:
http://printmoor.example/infopage?file=filetype_en&s=PrintMoor_new&lang=en
Industry/Entity Type
Business
Look and feel
Each slider illustrates characteristics of the customer's brand and the style your logo design should communicate.

```html
<!DOCTYPE html>
<html lang="en">
<head>
<meta charset="utf-8">
<title>The Ember Vale – Business Card</title>
<link href="https://fonts.googleapis.com/css2?family=Dosis:wght@300;400;600&display=swap" rel="stylesheet">
<style>
  :root {
    --brand-yellow: #fdcb16;
    --slate: #5f6b71;
    --charcoal: #2b2a29;
    --mist: #cfd3d6;
    --paper: #ffffff;
  }
  * { margin: 0; padding: 0; box-sizing: border-box; }
  html, body {
    width: 1200px; height: 412px; overflow: hidden;
    background: var(--paper);
    font-family: "Dosis", sans-serif;
  }
  .sheet { position: relative; width: 1200px; height: 412px; }

  .card {
    position: absolute; top: 56px;
    width: 531px; height: 288px; overflow: hidden;
  }
  .card--front { left: 29px; background: var(--brand-yellow); }
  .card--back { left: 640px; background: var(--slate); }

  /* Front */
  .front-mark {
    position: absolute; inset: 0;
    display: flex; align-items: center; justify-content: center; gap: 16px;
  }
  .front-mark__dot {
    width: 30px; height: 30px; border-radius: 50%; background: var(--slate);
  }
  .front-mark__name {
    font-weight: 600; font-size: 44px; color: var(--slate); letter-spacing: 1px;
  }

  /* Back */
  .name-banner { position: absolute; left: 158px; top: 45px; width: 373px; height: 77px; }
  .name-banner svg { position: absolute; inset: 0; }
  .name-banner__content {
    position: absolute; left: 36px; top: 0; height: 57px;
    display: flex; align-items: center; gap: 12px;
  }
  .name-banner__dot { width: 20px; height: 20px; border-radius: 50%; background: var(--brand-yellow); }
  .name-banner__name {
    font-weight: 600; font-size: 32px; color: var(--brand-yellow); letter-spacing: 1px;
  }

  .contact-list {
    position: absolute; left: 328px; top: 138px; list-style: none;
  }
  .contact-list li {
    display: flex; align-items: center; gap: 7px;
    height: 26.5px;
    font-weight: 400; font-size: 18px; color: var(--mist); letter-spacing: 1px;
  }
  .contact-list li::before {
    content: ""; width: 7px; height: 7px; background: var(--brand-yellow);
  }

  .web-band { position: absolute; left: 0; top: 247px; width: 297px; height: 41px; }
  .web-band svg { position: absolute; inset: 0; }
  .web-band__url {
    position: absolute; left: 62px; top: 5px;
    font-weight: 600; font-size: 20px; color: var(--slate);
  }
</style>
</head>
<body>
<main class="sheet">
  <section class="card card--front" aria-label="Card front">
    <div class="front-mark">
      <span class="front-mark__dot"></span>
      <span class="front-mark__name">The Ember Vale</span>
    </div>
  </section>

  <section class="card card--back" aria-label="Card back">
    <div class="name-banner">
      <svg width="373" height="77" viewBox="0 0 373 77">
        <polygon points="0,57 373,57 373,62 22,62" fill="#4b5459"/>
        <polygon points="0,0 373,0 373,57 22,57 22,75 0,55" fill="var(--charcoal)"/>
      </svg>
      <div class="name-banner__content">
        <span class="name-banner__dot"></span>
        <span class="name-banner__name">The Ember Vale</span>
      </div>
    </div>

    <ul class="contact-list">
      <li>000 000 000</li>
      <li>000 000 000</li>
      <li>Name@mail.com</li>
    </ul>

    <div class="web-band">
      <svg width="297" height="41" viewBox="0 0 297 41">
        <polygon points="0,0 279,0 297,18 297,41 0,41" fill="var(--brand-yellow)"/>
      </svg>
      <span class="web-band__url">www.embervale.example</span>
    </div>
  </section>
</main>
</body>
</html>
```